Business Card & Stationary Design Project

We are looking for some creative direction for business cards and our stationary.

We are a global logistics firm that has recently changed its name to Marrick Global Logistics and we have a new website due out tomorrow (www.marrick.com.au).

The colours of the company are rich navy tones, I would like to have business cards that fit together to make one picture on the back (possibly an old map of the world??), and the front to be modern contemporary looking.

But I am open to suggestions, so just incorporate our new logo and get going!
Updates

Hi Everyone,

Thank you for all of your designs so far and the time you have put into it.

I have asked many of you for amendments to see if we can get a final product, so with this in mind I am extending the deadline by a few days.

Good luck and thank you once again.

Please message me direct if you need any clarification.

Kind Regards
Colin

Reason: As outlined the extra 3 days is for amendments and changes to the current submissions. Thanks Colin

Industry/Entity Type

Business

```html
<!DOCTYPE html>
<html lang="en">
<head>
<meta charset="utf-8">
<title>Marrick Global Logistics – Business Card</title>
<link rel="stylesheet" href="https://fonts.googleapis.com/css2?family=Marcellus&family=Tinos:ital,wght@0,700;1,700&display=swap">
<style>
  :root {
    --page-bg: #e9edf2;
    --navy: #0f2a6b;
    --deep-blue: #1c4f93;
    --mid-blue: #3f7bbf;
    --pale-blue: #c9dcef;
    --card-light: #f4f8fc;
    --white: #ffffff;
  }
  * { box-sizing: border-box; margin: 0; padding: 0; }
  html, body { width: 1200px; height: 900px; overflow: hidden; }
  body {
    background: var(--page-bg);
    display: flex;
    flex-direction: column;
    align-items: center;
    justify-content: center;
    gap: 36px;
    font-family: "Marcellus", serif;
  }
  .card {
    position: relative;
    width: 700px;
    height: 400px;
    border-radius: 34px;
    overflow: hidden;
    box-shadow: 0 8px 22px rgba(15, 42, 107, 0.25);
  }
  .card-frame {
    position: absolute;
    inset: 14px;
    border: 3px solid var(--white);
    border-radius: 24px;
    pointer-events: none;
  }

  /* Back of card */
  .card-back {
    background: radial-gradient(ellipse at 55% 55%, #9fc2e6 0%, var(--mid-blue) 45%, var(--deep-blue) 85%);
  }
  .card-back .world-map {
    position: absolute;
    inset: 30px 40px 40px 40px;
    border-radius: 20px;
    background: radial-gradient(ellipse at 50% 45%, rgba(230, 240, 250, 0.75) 0%, rgba(220, 232, 244, 0.35) 55%, rgba(220, 232, 244, 0) 80%);
  }
  .back-wordmark {
    position: absolute;
    left: 0; right: 0;
    top: 170px;
    text-align: center;
    color: var(--navy);
    font-size: 50px;
    line-height: 1.2;
  }

  /* Front of card */
  .card-front {
    background: linear-gradient(180deg, var(--white) 0%, var(--card-light) 35%, var(--pale-blue) 70%, var(--mid-blue) 100%);
  }
  .card-front .world-map {
    position: absolute;
    inset: 70px 60px 60px 60px;
    border-radius: 20px;
    background: radial-gradient(ellipse at 50% 50%, rgba(255, 255, 255, 0.55) 0%, rgba(255, 255, 255, 0) 75%);
  }
  .front-logo {
    position: absolute;
    top: 42px;
    right: 48px;
    color: var(--navy);
    font-size: 28px;
    line-height: 1.2;
  }
  .contact-person {
    position: absolute;
    top: 138px;
    left: 0; right: 0;
    text-align: center;
    color: var(--navy);
  }
  .contact-person .person-name {
    font-size: 40px;
    letter-spacing: 2px;
  }
  .contact-person .person-title {
    font-size: 17px;
    letter-spacing: 1.5px;
    margin-top: 6px;
  }
  .contact-details {
    position: absolute;
    left: 48px;
    right: 48px;
    bottom: 54px;
    display: flex;
    justify-content: space-between;
    align-items: flex-end;
    font-family: "Tinos", serif;
    font-weight: 700;
    color: var(--white);
    font-size: 24px;
    line-height: 1.25;
    text-shadow: 0 1px 2px rgba(15, 42, 107, 0.35);
  }
  .phone-list { display: grid; grid-template-columns: auto auto; column-gap: 22px; }
  .phone-list dt { font-style: italic; }
  .web-list { text-align: right; }
</style>
</head>
<body>

  <section class="card card-back" aria-label="Business card back">
    <div class="world-map" role="img" aria-label="World map in pale blue across the card"></div>
    <div class="back-wordmark">Marrick Global Logistics</div>
    <div class="card-frame"></div>
  </section>

  <section class="card card-front" aria-label="Business card front">
    <div class="world-map" role="img" aria-label="Faint world map behind the contact details"></div>
    <div class="front-logo">Marrick Global Logistics</div>
    <div class="contact-person">
      <div class="person-name">Derek Halloway</div>
      <div class="person-title">Senior Manager</div>
    </div>
    <div class="contact-details">
      <dl class="phone-list">
        <dt>Phone:</dt><dd>123–480–7731</dd>
        <dt>Cell:</dt><dd>121–906–4428</dd>
      </dl>
      <div class="web-list">
        <div>Derek@marrick.com.au</div>
        <div>www.marrick.com.au</div>
      </div>
    </div>
    <div class="card-frame"></div>
  </section>

</body>
</html>
```